Bramlow Films, LLC needs a business card with a great Toucan Graphic!

Our current business card has a graphic image of a Toucan bird as a play on the word "Bramlow" which is a small independent film company located here in California. I have been using this image as a mockup, but it is a copyrighted image, so we need something that is original art which will not put us in jeopardy down the road...

We definitely still want an image of a toucan however (not, as some have suggested, two "cans" of film or some other play on the word).

I have uploaded a pdf file of my OLD business card.

Thanks and look forward to reviewing the designs!

Dean

Target Market(s)

Filmmakers, distribution and production executives, other professionals in the filmmaking world,

Industry/Entity Type

Business

Contact Information for Business Card

Dean Whitcomb, Writer/Director
Bramlow Films, LLC
417 Heron Ridge Lane
Del Mar, California 92014

Cell: 415.293.6051
Email: dean@bramlowfilms.com

Font styles to use
Sans Serif

Requirements
Must have
• A toucan bird as our logo. Bramlow Films, LLC (capital T and C in Bramlow)
Should not have
• Anything else other than a toucan bird as a play on the word "Bramlow"

```html
<!DOCTYPE html>
<html lang="en">
<head>
<meta charset="utf-8">
<title>Bramlow Films LLC — Business Card</title>
<link rel="stylesheet" href="https://fonts.googleapis.com/css2?family=Questrial&family=Arimo:wght@400&display=swap">
<style>
  :root {
    --teal: #17b3aa;
    --teal-deep: #0f9c94;
    --teal-light: #7fdcd5;
    --ink: #1a1a1a;
    --paper: #ffffff;
    --backdrop: #ecebe8;
  }
  html, body {
    margin: 0;
    width: 1200px;
    height: 900px;
    overflow: hidden;
    background: var(--backdrop);
  }
  .canvas {
    width: 1200px;
    height: 900px;
    display: flex;
    align-items: center;
    justify-content: center;
    gap: 40px;
  }
  .card {
    width: 540px;
    height: 309px;
    position: relative;
    box-shadow: 0 2px 10px rgba(0, 0, 0, 0.12);
    overflow: hidden;
    flex: 0 0 auto;
  }
  .card-back {
    background: var(--teal);
    display: flex;
    align-items: center;
    justify-content: center;
  }
  .card-back .brand-name {
    font-family: "Questrial", sans-serif;
    font-size: 30px;
    color: var(--paper);
    letter-spacing: 0.5px;
    margin: 0 30px 0 0;
  }
  .card-front {
    background: var(--paper);
    display: flex;
  }
  .info {
    flex: 0 0 51%;
    padding: 26px 0 0 18px;
    box-sizing: border-box;
    position: relative;
  }
  .info .brand-name {
    font-family: "Questrial", sans-serif;
    font-size: 24px;
    line-height: 1.1;
    color: var(--teal);
    margin: 0 0 16px;
    white-space: nowrap;
  }
  .person-name {
    font-family: "Arimo", sans-serif;
    font-size: 23px;
    line-height: 1.1;
    color: var(--ink);
    margin: 0;
    white-space: nowrap;
  }
  .person-title {
    font-family: "Arimo", sans-serif;
    font-size: 14px;
    line-height: 1.2;
    color: var(--ink);
    margin: 4px 0 0;
  }
  .contact {
    position: absolute;
    left: 18px;
    right: 6px;
    bottom: 26px;
    font-family: "Arimo", sans-serif;
    font-size: 11.5px;
    line-height: 1.3;
    color: var(--ink);
    margin: 0;
  }
  .mascot-panel {
    flex: 1;
    background: radial-gradient(ellipse at 55% 50%, var(--teal-light) 0%, var(--teal) 60%, var(--teal-deep) 100%);
  }
</style>
</head>
<body>
  <main class="canvas">
    <section class="card card-back" aria-label="Card back">
      <p class="brand-name">Bramlow Films LLC</p>
    </section>

    <section class="card card-front" aria-label="Card front">
      <div class="info">
        <p class="brand-name">Bramlow Films LLC</p>
        <p class="person-name">Dean Whitcomb</p>
        <p class="person-title">Writer/Director</p>
        <p class="contact">
          417 Heron Ridge Lane Del Mar,<br>
          California 92014<br>
          Cell: 415.293.6051<br>
          Email: dean@bramlowfilms.com
        </p>
      </div>
      <div class="mascot-panel" role="img" aria-label="Toucan illustration: a black and white toucan perched in front of swirling pale teal leaf shapes"></div>
    </section>
  </main>
</body>
</html>
```